Digital Album Cover - Quiet Frost (Candles Burning)

HiI need a digital album cover for a piano instrumental cover single

Artist: Toby Halvern
Title: Quiet Frost (Candles Burning)

The song was originally by Carl Dupree

Please use my logo

You can listen to the track herehttps://soundcloud.com/tobyhalvernpianist/quiet-frost-candles-burning-piano-instrumental-cover

Requirements
Must have
• My logo design Toby Halvern

```html
<!DOCTYPE html>
<html lang="en">
<head>
<meta charset="utf-8">
<title>Quiet Frost (Candles Burning) – Toby Halvern</title>
<link rel="stylesheet" href="https://fonts.googleapis.com/css2?family=Bangers&family=Open+Sans:ital,wght@0,400;0,700;1,700&display=swap">
<style>
  :root {
    --page-bg: #3a3a3a;
    --sky-top: #5a2810;
    --sky-mid: #b9531f;
    --sky-low: #d06a2c;
    --ground: #160a04;
    --sun-core: #f4a866;
    --sun-edge: rgba(232, 140, 80, 0);
    --ink-light: #ffffff;
  }
  html, body {
    margin: 0;
    padding: 0;
    width: 1200px;
    height: 900px;
    overflow: hidden;
    background: var(--page-bg);
  }
  .album-cover {
    position: absolute;
    left: 110px;
    top: 28px;
    width: 980px;
    height: 844px;
    overflow: hidden;
    font-family: "Open Sans", Arial, sans-serif;
    color: var(--ink-light);
  }
  .cover-artwork {
    position: absolute;
    inset: 0;
    width: 100%;
    height: 100%;
  }
  .brand {
    position: absolute;
    left: 44px;
    top: 29px;
    display: flex;
    align-items: center;
    gap: 10px;
  }
  .brand-dot {
    width: 70px;
    height: 70px;
    border-radius: 50%;
    background: var(--ink-light);
  }
  .brand-text {
    display: flex;
    flex-direction: column;
    line-height: 1.1;
  }
  .brand-name {
    font-size: 27px;
    font-weight: 700;
    letter-spacing: 0.5px;
    text-transform: uppercase;
  }
  .brand-tagline {
    font-size: 13px;
    font-weight: 400;
    margin-left: 25px;
  }
  .title-block {
    position: absolute;
    left: 329px;
    top: 120px;
    width: 400px;
    text-align: center;
    font-family: "Bangers", "Impact", sans-serif;
    font-style: normal;
  }
  .title-main {
    margin: 0;
    font-size: 100px;
    line-height: 118px;
    font-weight: 400;
    letter-spacing: 3px;
  }
  .title-sub {
    margin: 8px 0 0;
    font-size: 44px;
    letter-spacing: 2px;
    font-weight: 400;
  }
  .credit {
    position: absolute;
    left: 0;
    right: 0;
    top: 796px;
    margin: 0;
    text-align: center;
    font-size: 19px;
    font-weight: 700;
    font-style: italic;
  }
</style>
</head>
<body>
  <main class="album-cover">
    <svg class="cover-artwork" viewBox="0 0 980 844" role="img"
         aria-label="Sunset illustration: orange sky with a large glowing sun, layered mountain silhouettes, a lone figure walking through grass and a grand piano with bench floating beside the sun">
      <defs>
        <linearGradient id="sky" x1="0" y1="0" x2="0" y2="1">
          <stop offset="0" stop-color="var(--sky-top)"/>
          <stop offset="0.45" stop-color="var(--sky-mid)"/>
          <stop offset="0.68" stop-color="var(--sky-low)"/>
          <stop offset="0.8" stop-color="#6e3114"/>
          <stop offset="0.9" stop-color="var(--ground)"/>
          <stop offset="1" stop-color="#000"/>
        </linearGradient>
        <radialGradient id="sun" cx="0.5" cy="0.5" r="0.5">
          <stop offset="0" stop-color="var(--sun-core)"/>
          <stop offset="0.95" stop-color="#e58c4f" stop-opacity="0.55"/>
          <stop offset="1" stop-color="var(--sun-edge)"/>
        </radialGradient>
      </defs>
      <rect width="980" height="844" fill="url(#sky)"/>
      <circle cx="529" cy="290" r="214" fill="url(#sun)"/>
    </svg>

    <header class="brand">
      <span class="brand-dot"></span>
      <span class="brand-text">
        <span class="brand-name">Toby Halvern</span>
        <span class="brand-tagline">Wedding &amp; Event Pianist</span>
      </span>
    </header>

    <section class="title-block">
      <h1 class="title-main">QUIET<br>FROST</h1>
      <p class="title-sub">(CANDLES BURNING)</p>
    </section>

    <p class="credit">The song was originally by Carl Dupree</p>
  </main>
</body>
</html>
```